Thistle Ridge Bourbon Barrel Aged Wine

We are taking a sweet red wine and barrel aging it in previously used bourbon barrels. The abv is 16%. Kentucky based. I have attached our Brand logo for reference. Use colors that evoke warmth, richness, and sophistication. We would like to consider a raised or textured label.

Target Market(s)

bourbon and wine drinkers

```html
<!DOCTYPE html>
<html lang="en">
<head>
<meta charset="utf-8">
<title>Thistle Ridge Red Wine Blend – Labels</title>
<link rel="stylesheet" href="https://fonts.googleapis.com/css2?family=Cinzel:wght@400;600&family=Archivo+Narrow:wght@600;700&display=swap">
<style>
  :root {
    --bg: #151315;
    --label: #2b2a2c;
    --label-dark: #1f1e20;
    --silver: #d9d9d9;
    --silver-dim: #a8a8a8;
    --wine-red: #c9283f;
  }
  * { box-sizing: border-box; margin: 0; padding: 0; }
  html, body { width: 1200px; height: 1200px; overflow: hidden; }
  body {
    background: var(--bg);
    font-family: "Cinzel", serif;
    color: var(--silver);
    position: relative;
  }

  /* Front label */
  .front-label {
    position: absolute;
    left: 60px; top: 190px;
    width: 500px; height: 820px;
  }
  .front-label .label-shape { position: absolute; inset: 0; }
  .front-label .label-content {
    position: absolute; inset: 0;
    text-align: center;
  }
  .brand-mark {
    position: absolute; top: 150px; left: 0; right: 0;
    display: flex; align-items: center; justify-content: center; gap: 12px;
    font-size: 24px; font-weight: 600; letter-spacing: 3px; text-transform: uppercase;
  }
  .brand-mark .mark-dot {
    width: 16px; height: 16px; border-radius: 50%; background: var(--silver);
  }
  .front-title {
    position: absolute; top: 315px; left: 0; right: 0;
    font-size: 46px; font-weight: 600; letter-spacing: 2px; text-transform: uppercase;
  }
  .front-subtitle {
    position: absolute; top: 380px; left: 0; right: 0;
    font-size: 36px; color: var(--wine-red); letter-spacing: 2px; text-transform: uppercase;
  }
  .front-aged {
    position: absolute; top: 440px; left: 0; right: 0;
    font-size: 23px; font-weight: 600; line-height: 1.2; letter-spacing: 1.5px; text-transform: uppercase;
  }
  .front-volume {
    position: absolute; top: 560px; left: 110px;
    font-size: 18px; font-weight: 600; line-height: 1.3; text-align: left; text-transform: uppercase;
  }

  /* Back label */
  .back-label {
    position: absolute;
    left: 640px; top: 210px;
    width: 500px; height: 780px;
    background: var(--label);
    border: 3px solid var(--silver);
    outline: 1px solid var(--silver-dim);
    outline-offset: -14px;
    padding: 42px 40px;
    text-align: center;
  }
  .back-label .corner {
    position: absolute; width: 26px; height: 26px;
    border: 2px solid var(--silver); background: var(--label-dark);
  }
  .corner.tl { top: -4px; left: -4px; }
  .corner.tr { top: -4px; right: -4px; }
  .corner.bl { bottom: -4px; left: -4px; }
  .corner.br { bottom: -4px; right: -4px; }
  .back-title {
    font-size: 38px; font-weight: 600; letter-spacing: 2px; text-transform: uppercase;
  }
  .back-subtitle {
    font-size: 26px; color: var(--wine-red); letter-spacing: 1.5px; text-transform: uppercase;
    margin-top: 2px;
  }
  .back-story {
    margin-top: 22px;
    font-family: "Archivo Narrow", sans-serif; font-weight: 700;
    font-size: 12.5px; line-height: 1.45; text-transform: uppercase; letter-spacing: 0.3px;
  }
  .back-bottling {
    margin-top: 22px;
    font-size: 17px; font-weight: 600; line-height: 1.25; text-transform: uppercase;
  }
  .back-warning {
    margin-top: 26px; text-align: left;
    font-family: "Archivo Narrow", sans-serif; font-weight: 700;
    font-size: 15px; line-height: 1.35; text-transform: uppercase;
  }
  .back-sulfites {
    margin-top: 16px; text-align: left;
    font-family: "Archivo Narrow", sans-serif; font-weight: 700;
    font-size: 22px; letter-spacing: 0.5px; text-transform: uppercase;
  }
</style>
</head>
<body>

<section class="front-label">
  <svg class="label-shape" width="500" height="820" viewBox="0 0 500 820">
    <defs>
      <linearGradient id="artTone" x1="0" y1="0" x2="0" y2="1">
        <stop offset="0" stop-color="#3a393b"/>
        <stop offset="1" stop-color="#6e6d70"/>
      </linearGradient>
      <clipPath id="frontClip">
        <path d="M250,14 C430,130 486,300 486,420 C486,560 410,712 250,806 C90,712 14,560 14,420 C14,300 70,130 250,14 Z"/>
      </clipPath>
    </defs>
    <path d="M250,0 C440,120 500,300 500,420 C500,565 420,725 250,820 C80,725 0,565 0,420 C0,300 60,120 250,0 Z" fill="#d9d9d9"/>
    <path d="M250,14 C430,130 486,300 486,420 C486,560 410,712 250,806 C90,712 14,560 14,420 C14,300 70,130 250,14 Z" fill="#2b2a2c"/>
    <g clip-path="url(#frontClip)">
      <rect x="0" y="640" width="500" height="180" fill="url(#artTone)" role="img" aria-label="Engraved silver illustration of rolling Kentucky hills"/>
    </g>
  </svg>
  <div class="label-content">
    <div class="brand-mark"><span class="mark-dot"></span><span>Thistle Ridge</span></div>
    <h1 class="front-title">Thistle Ridge</h1>
    <p class="front-subtitle">Red Wine Blend</p>
    <p class="front-aged">Aged in Kentucky<br>Bourbon Barrels</p>
    <p class="front-volume">16% ABV<br>750 ML</p>
  </div>
</section>

<section class="back-label">
  <span class="corner tl"></span><span class="corner tr"></span>
  <span class="corner bl"></span><span class="corner br"></span>
  <h2 class="back-title">Thistle Ridge</h2>
  <p class="back-subtitle">Red Wine Blend</p>
  <p class="back-story">
    Experience the unique fusion of a red wine blend aged in Kentucky bourbon barrels by Thistle Ridge Distillery.
    Indulge in the captivating blend with rich notes of blackberries, cherries, and vanilla, with a velvety texture and a hint of smoky bourbon.
    Indulge in this harmonious symphony of flavors where wine and bourbon unite in perfect balance.
    The initial sip unveils a velvety texture, with notes of plum and currant dancing on the tongue. As the wine evolves, a gentle undercurrent of smoky bourbon essence emerges, adding layers of complexity to the experience.
    The finish is long and luxurious, with soft tannins and a lingering essence of toasted oak and spice.
  </p>
  <p class="back-bottling">
    Barrel aged and bottled at<br>Thistle Ridge Distillery Cedar Bend, KY.<br>750 ML Alc. 16% by vol
  </p>
  <p class="back-warning">
    Government warning: (1) According to the Surgeon General, women should not drink alcoholic beverages during pregnancy because of the risk of birth defects. (2) Consumption of alcoholic beverages impairs your ability to drive a car or operate machinery, and may cause health problems.
  </p>
  <p class="back-sulfites">Contains sulfites</p>
</section>

</body>
</html>
```